Design a Website Mockup for CounselBidHub.com

[url removed, login to view] is a website we are building where Clients can post a brief summary of their case and Attorneys can bid on the job--this way the client gets the best Attorney for the least amount of money. This site will be basically a combination of a site like this one and Lawful Nest. We bought a script and it is uploaded at CounselBidHub.com. The script is basically just a framework that we are working from. Please find the powerpoint presentation attached that is just a framework to work form for each of the pages listed in the presentation. The logo will be bigger than it currently appears on the site. But please incorporate the logo where you feel it should be. The current colors of the site are off. But we would like the colors to be similar to those that are in the logo. Basically we're going for a clean, classic American attorney look and feel for the site. The design colors should be brown, green and gold. But where our clients need to input text should be mostly white like this page.

PLEASE NOTE: We just uploaded "A rough draft of the homepage" this is a compilation of all of the elements that we have liked from your submissions. If you see one of your elements in our final draft you will be compensated a fair amount for that element if you're not the winner.

*A winner is Guaranteed
*If we see pages that we like from other applicants we will compensate you if we decide to use any of your pages on a single basis.

```html
<!DOCTYPE html>
<html lang="en">
<head>
<meta charset="utf-8">
<title>CounselBidHub.com</title>
<link href="https://fonts.googleapis.com/css2?family=Cinzel:wght@400;700&family=Mulish:wght@400&family=Open+Sans:wght@400;600&family=Lato:wght@400&display=swap" rel="stylesheet">
<style>
:root{
  --cream:#fdf5e6;
  --cream-deep:#f6e8cc;
  --brown-dark:#3d1f0b;
  --brown:#6b3814;
  --brown-mid:#8a4c22;
  --brown-light:#a4683a;
  --gold:#f3ddb0;
  --text:#4a3626;
  --icon-grey:#8e8580;
  --white:#ffffff;
}
*{margin:0;padding:0;box-sizing:border-box}
html,body{width:1200px;height:833px;overflow:hidden;background:var(--cream)}
.page{position:relative;width:1200px;height:833px;font-family:"Mulish",sans-serif;color:var(--text)}
.world-map{position:absolute;left:430px;top:0;width:380px;height:130px;border-radius:40px;
  background:radial-gradient(ellipse at center,#f4deaa 0%,rgba(244,222,170,.4) 55%,rgba(253,245,230,0) 75%)}
.brand{position:absolute;left:228px;top:52px;display:flex;align-items:center;gap:10px;
  font-family:"Cinzel",serif;font-weight:700;font-size:26px;color:var(--brown)}
.brand-mark{width:34px;height:34px;border-radius:50%;background:var(--brown-mid)}
.country-select{position:absolute;left:844px;top:28px;width:136px;height:22px;border:1px solid #cbb9a0;background:var(--white);
  font-family:"Open Sans",sans-serif;font-size:12px;color:#333;display:flex;align-items:center;padding-left:6px;gap:6px}
.country-select .flag{width:16px;height:11px;background:linear-gradient(#b22 0 50%,#eee 50%)}
.country-select .caret{margin-left:auto;margin-right:6px;border:4px solid transparent;border-top-color:#777;margin-top:4px}
.social{position:absolute;display:flex;gap:4px}
.social span{display:block;border-radius:50%;background:var(--icon-grey)}
.social.top{left:858px;top:71px}
.social.top span{width:23px;height:23px}
.phone{position:absolute;left:842px;top:104px;font-family:"Cinzel",serif;font-size:25px;color:var(--brown-mid)}
.main-nav{position:absolute;left:201px;top:146px;width:797px;height:34px;display:flex;border-radius:3px;
  background:linear-gradient(#a0643a,#7a4119);box-shadow:0 2px 3px rgba(0,0,0,.25)}
.main-nav a{display:flex;align-items:center;justify-content:center;color:#f5e6d0;text-decoration:none;
  font-family:"Open Sans",sans-serif;font-size:13px;border-right:1px solid rgba(255,255,255,.18)}
.main-nav a:last-child{border-right:0}
.main-nav a.active{background:linear-gradient(#6a3410,#4a220a);border-radius:3px 0 0 3px}
.faint-name{position:absolute;left:0;width:1200px;top:378px;text-align:center;font-family:"Cinzel",serif;font-size:64px;
  color:rgba(160,110,60,.07);font-weight:700;white-space:nowrap;z-index:0}
.cta{position:absolute;top:320px;height:56px;border-radius:28px;border:3px solid var(--white);z-index:1;
  background:linear-gradient(#7a3c16,#3d1a06);box-shadow:0 2px 5px rgba(0,0,0,.25);display:flex;align-items:center;
  font-family:"Cinzel",serif;font-size:19px;line-height:1;white-space:nowrap;color:var(--gold);text-decoration:none;overflow:hidden}
.cta .avatar{flex:none;width:44px;height:44px;border-radius:50%;background:#f2ede6;border:2px solid #c9a77d;margin-left:4px;margin-right:14px}
.cta.attorney{left:313px;width:265px}
.cta.hire{left:622px;width:264px}
.cta.hire .avatar{margin-right:10px}
.welcome{position:absolute;left:0;width:1200px;top:458px;text-align:center;font-family:"Cinzel",serif;font-weight:700;
  font-size:29px;color:var(--brown-dark)}
.intro{position:absolute;left:201px;top:508px;width:779px;font-size:15.5px;line-height:24px;text-align:justify}
.site-footer{position:absolute;left:0;top:652px;width:1200px;height:136px;background:linear-gradient(#8a4c22,#4a240c)}
.footer-col{position:absolute;top:18px;color:var(--white)}
.footer-col h3{font-family:"Lato",sans-serif;font-weight:400;font-size:17px;margin-bottom:14px}
.footer-col ul{list-style:none}
.footer-col li{font-family:"Open Sans",sans-serif;font-weight:600;font-size:11.5px;margin-bottom:8px;padding-left:15px;position:relative;white-space:nowrap}
.footer-col li::before{content:"";position:absolute;left:0;top:4px;border:3px solid transparent;border-left:4px solid #e0a060}
.divider{position:absolute;top:18px;width:1px;height:100px;background:rgba(0,0,0,.25);box-shadow:1px 0 0 rgba(255,255,255,.1)}
.lang-select{width:160px;height:20px;background:var(--white);border:1px solid #999;font-family:"Open Sans",sans-serif;
  font-size:11px;color:#444;display:flex;align-items:center;padding-left:7px;margin-top:-1px}
.lang-select .btn{margin-left:auto;width:18px;height:18px;background:#eee;border-left:1px solid #999;display:flex;align-items:center;justify-content:center}
.lang-select .btn i{border:4px solid transparent;border-top-color:#222;margin-top:4px}
.social.footer{position:static}
.social.footer span{width:28px;height:28px;background:#a29b97}
.copyright{position:absolute;left:0;width:1200px;top:803px;text-align:center;font-family:"Open Sans",sans-serif;font-size:12px;color:#5a4636}
</style>
</head>
<body>
<div class="page">
  <header>
    <div class="world-map" role="img" aria-label="Faint world map backdrop"></div>
    <div class="brand"><span class="brand-mark"></span>CounselBidHub.com</div>
    <div class="country-select"><span class="flag" role="img" aria-label="US flag"></span>USA<span class="caret"></span></div>
    <div class="social top"><span></span><span></span><span></span><span></span></div>
    <div class="phone">123-456-7890</div>
    <nav class="main-nav">
      <a class="active" style="width:96px">Home</a>
      <a style="width:151px">Find Attorney</a>
      <a style="width:122px">Post Case</a>
      <a style="width:127px">Market Place</a>
      <a style="width:118px">Law Firms</a>
      <a style="width:80px">Jobs</a>
      <a style="width:103px">News</a>
    </nav>
  </header>

  <main>
    <div class="faint-name">CounselBidHub</div>
    <a class="cta attorney"><span class="avatar" role="img" aria-label="Attorney icon"></span>I'm an Attorney</a>
    <a class="cta hire"><span class="avatar" role="img" aria-label="Client icon"></span>Hire An Attroney</a>
    <h1 class="welcome">Welcome to CounselBid Hub</h1>
    <p class="intro">CounselBidHub.com is the premier destination for clients to hire the best attorneys at the best rate. CounselBidHub helps Attorneys to grow their business, hire staff, find like-minded attorneys for partnership, shop for office products, get legal news and updates, and much more. Clients can find legal forms and form legal entities, trademark, and file other legal matters directly on our site.</p>
  </main>

  <footer class="site-footer">
    <div class="footer-col" style="left:238px">
      <h3>Shortcut</h3>
      <ul><li>Find Attorneys and more</li><li>Find Legal Work</li><li>How it Works</li></ul>
    </div>
    <div class="divider" style="left:418px"></div>
    <div class="footer-col" style="left:455px">
      <h3>About Us</h3>
      <ul><li>About Us</li><li>Terms and Conditions</li></ul>
    </div>
    <div class="divider" style="left:614px"></div>
    <div class="footer-col" style="left:647px">
      <h3>Language</h3>
      <div class="lang-select">English<span class="btn"><i></i></span></div>
    </div>
    <div class="divider" style="left:824px"></div>
    <div class="footer-col" style="left:838px">
      <h3>Foollow Us</h3>
      <div class="social footer"><span></span><span></span><span></span><span></span></div>
    </div>
  </footer>
  <p class="copyright">© Copyright 2013 CounselBidHub.com. All Right Reserved.</p>
</div>
</body>
</html>
```